Real Estate Webpage Design

We have an existing website: verindaleestates.com.au
We focus customised service mainly on Property Management and second-hand property sales.
We are not entirely happy about the current design and layout can stay roughly the same as the back end coding is linked to a CRM system.
We would like to see the design are more reachable to our clients and appearing.
Please check our Website Design Draft for more details.

Industry/Entity Type

Real estate Agency

Number of Pages Required

5+ page

Font styles to use
Sans Serif

Colors

Designer to choose colors to be used in the design.

```html
<!DOCTYPE html>
<html lang="en">
<head>
<meta charset="utf-8">
<title>Verindale Estates – Real Estate Agency</title>
<link href="https://fonts.googleapis.com/css2?family=Poppins:wght@300;400;500;600&display=swap" rel="stylesheet">
<style>
:root{
  --gold:#efb940;
  --gold-dark:#d9a22a;
  --ink:#1f2330;
  --text:#6f7380;
  --navy:#1e3150;
  --cream:#fbeccb;
  --grey:#f6f6f8;
  --line:#e3e3e8;
  --white:#fff;
}
*{box-sizing:border-box;margin:0;padding:0}
html,body{width:1200px;height:5343px;overflow:hidden}
body{font-family:'Poppins',sans-serif;color:var(--ink);background:var(--white);position:relative}
.abs{position:absolute}
.btn{display:inline-block;background:var(--gold);color:var(--white);font-size:13px;padding:8px 18px;border:2px solid #fff;outline:1px solid var(--gold)}
.btn-ghost{display:inline-block;background:#fff;color:var(--ink);font-size:13px;padding:8px 18px;border:1px solid var(--line)}
.h2{font-size:27px;font-weight:600;text-align:center;color:var(--ink)}
.brand{display:flex;align-items:center;gap:10px;font-weight:500;color:var(--gold);font-size:24px}
.brand .mark{width:30px;height:30px;background:var(--gold)}
/* header */
.site-header{top:0;left:0;width:1200px;height:62px;background:#fff;z-index:3}
.logo-box{top:0;left:62px;width:222px;height:75px;background:#fff;display:flex;align-items:center;padding-left:16px;z-index:4}
.nav{top:22px;left:433px;display:flex;gap:30px;font-size:13px;color:var(--ink);z-index:4}
.nav .active{color:var(--gold);border-bottom:2px solid var(--gold);padding-bottom:16px}
.nav-cta{top:16px;left:1012px;z-index:4;font-size:13px;padding:7px 16px}
/* hero */
.hero{top:62px;left:0;width:1200px;height:612px;background:linear-gradient(180deg,#b8c7d6 0%,#8e9aa5 45%,#5e6250 75%,#4e6a34 100%)}
.hero-title{top:245px;left:60px;font-size:38px;font-weight:500;color:var(--gold);line-height:50px}
.hero-text{top:350px;left:60px;font-size:13px;color:#fff;line-height:23px;width:560px}
.search{top:438px;left:60px;width:480px;height:50px;background:#fff;display:flex}
.search .f{padding:6px 10px;border-right:1px solid var(--line)}
.search .f small{display:block;font-size:9px;color:var(--gold)}
.search .f span{font-size:11px;color:var(--ink)}
.search .go{width:48px;background:var(--gold);display:flex;align-items:center;justify-content:center}
/* why */
.why-title{top:752px;left:0;width:1200px}
.features{top:820px;left:170px;width:860px;display:flex}
.feature{flex:1;text-align:center;padding:0 18px}
.feature svg{height:64px}
.feature h3{font-size:16px;font-weight:500;margin:14px 0 8px}
.feature p{font-size:12.5px;color:var(--text);line-height:23px}
/* services */
.photo{display:block}
.svc-text h3{font-size:26px;font-weight:500;margin-bottom:36px}
.svc-text p{font-size:12.5px;color:var(--text);line-height:23px;margin-bottom:22px}
.svc-text .btn{font-size:12px;padding:6px 16px}
/* save */
.save-card{width:260px;height:130px;background:var(--grey);text-align:center;padding-top:24px}
.save-card small{font-size:11px;display:block}
.save-card b{display:block;font-size:26px;font-weight:500;margin:4px 0}
.save-card span{font-size:12px}
/* listings */
.listings{top:2803px;left:0;width:1200px;height:742px;background:var(--grey)}
.tabs{top:2917px;left:334px;display:flex}
.tabs div{width:106px;height:35px;border:1px solid #cfcfd6;background:#fff;font-size:13px;display:flex;align-items:center;justify-content:center}
.tabs .on{background:var(--gold);color:#fff;border-color:var(--gold)}
.card{width:342px;height:415px;background:#fff;top:2985px}
.card .tag{position:absolute;top:0;left:0;background:var(--navy);color:#fff;font-size:11px;padding:3px 8px;z-index:2}
.card .img{position:absolute;top:12px;left:10px;width:322px;height:178px}
.card .price{position:absolute;top:157px;left:22px;color:#fff;font-size:15px;font-weight:500}
.card .body{position:absolute;top:195px;left:20px;right:20px}
.card h4{font-size:16px;font-weight:500}
.card .addr{font-size:12px;margin:6px 0 12px;display:flex;gap:6px;align-items:center}
.card .feat{display:flex;gap:14px;font-size:12px;color:var(--ink);align-items:center}
.card .insp{font-size:15px;font-weight:500;margin-top:20px}
.card .date{font-size:12px;color:var(--gold);margin-top:4px}
.card .agent{position:absolute;bottom:0;left:0;right:0;height:56px;border-top:1px solid var(--line);display:flex;align-items:center;padding:0 14px;gap:12px;font-size:12px}
.avatar{width:30px;height:30px;background:#c7c2bc}
.card .tools{margin-left:auto;display:flex;gap:8px}
.arrow{width:30px;height:30px;border:1px solid var(--gold);display:flex;align-items:center;justify-content:center;background:#fff}
.arrow.fill{background:var(--gold)}
/* who */
.who-photo{top:3545px;left:0;width:1200px;height:597px;background:linear-gradient(180deg,#c9ccce 0%,#aab0ae 45%,#5f7548 80%,#4b5a3e 100%)}
.who-box{top:3905px;left:60px;width:1080px;height:432px;background:var(--cream);text-align:center;padding-top:50px}
.who-box h2{font-size:26px;font-weight:600;margin-bottom:24px}
.who-box p{font-size:12.5px;color:var(--text);line-height:23px;width:700px;margin:0 auto 16px}
.who-box .note{color:var(--gold);font-size:11.5px;width:760px}
/* contact band */
.cta{top:4782px;left:0;width:1200px;height:226px;background:var(--navy);text-align:center;padding-top:50px;color:#fff}
.cta h2{font-size:23px;font-weight:500;line-height:38px;margin-bottom:22px}
/* footer */
.footer h5{font-size:13px;color:var(--gold);font-weight:400;margin-bottom:18px}
.footer li{list-style:none;font-size:12px;line-height:27px}
.footer p{font-size:12px;line-height:22px}
.social{display:flex;gap:16px}
.social div{width:38px;height:38px;border-radius:50%;border:1px solid var(--line)}
.social .first{background:var(--gold);border-color:var(--gold)}
.bottom-bar{top:5300px;left:60px;width:1080px;font-size:11px;display:flex;justify-content:space-between}
.bottom-bar nav{display:flex;gap:26px}
</style>
</head>
<body>

<header class="site-header abs"></header>
<div class="logo-box abs"><div class="brand"><span class="mark"></span>Verindale Estates</div></div>
<nav class="nav abs">
  <span class="active">Home</span><span>About Us</span><span>Leasing</span><span>Buy</span><span>Sell</span><span>Our Team</span><span>Blog</span><span>Contact Us</span>
</nav>
<a class="btn nav-cta abs">Add Properties</a>

<section class="hero abs" role="img" aria-label="Modern two-storey concrete home with lawn under a cloudy sky"></section>
<h1 class="hero-title abs">Welcome To Verindale<br>Estates</h1>
<p class="hero-text abs">Lorem ipsum is simply dummy text of the printing and typesetting industry. Lorem ipsum has been the industry's standard dummy text ever since the 1500s, when an unknown printer</p>
<div class="search abs">
  <div class="f" style="width:105px"><small>I WANT TO</small><span>Buy House</span></div>
  <div class="f" style="flex:1;border:0"><small>Location</small><span style="color:#888">Enter Street adress,city,town,zip,school district...</span></div>
  <div class="go"><svg width="20" height="20" viewBox="0 0 20 20" fill="none" stroke="#fff" stroke-width="2"><circle cx="8" cy="8" r="6"/><path d="M13 13l5 5"/></svg></div>
</div>

<h2 class="h2 why-title abs">Why People Choose Verindale Estates?</h2>
<div class="features abs">
  <div class="feature">
    <svg viewBox="0 0 64 64" fill="none" stroke="#1e3150" stroke-width="2"><circle cx="32" cy="26" r="7"/><circle cx="16" cy="32" r="6"/><circle cx="48" cy="32" r="6"/><path d="M20 58v-8a12 12 0 0 1 24 0v8M4 58v-6a10 10 0 0 1 14-9M60 58v-6a10 10 0 0 0-14-9"/><path d="M32 4l2 4 4 1-3 3 1 4-4-2-4 2 1-4-3-3 4-1z" stroke="#efb940"/></svg>
    <h3>Great Experience</h3>
    <p>Lorem ipsum is simply dummy text of the printing and typesetting industry. Lorem Ipsum has been the industry's standard dummy text</p>
  </div>
  <div class="feature">
    <svg viewBox="0 0 64 64" fill="none" stroke="#1e3150" stroke-width="2"><rect x="6" y="26" width="52" height="30"/><path d="M14 42l10-8 8 6 8-6 10 8M24 34l8 8"/><rect x="26" y="6" width="12" height="14" stroke="#efb940"/></svg>
    <h3>Safety Deals</h3>
    <p>Lorem ipsum is simply dummy text of the printing and typesetting industry. Lorem Ipsum has been the industry's standard dummy text</p>
  </div>
  <div class="feature">
    <svg viewBox="0 0 64 64" fill="none" stroke="#1e3150" stroke-width="2"><circle cx="30" cy="34" r="14"/><path d="M14 34a16 16 0 0 1 32 0M12 32h4v8h-4zM44 32h4v8h-4zM16 60a14 14 0 0 1 28 0"/><circle cx="50" cy="14" r="8" stroke="#efb940"/></svg>
    <h3>Comprehensive Support</h3>
    <p>Lorem ipsum is simply dummy text of the printing and typesetting industry. Lorem Ipsum has been the industry's standard dummy text</p>
  </div>
</div>

<div class="photo abs" style="top:1103px;left:60px;width:541px;height:464px;background:linear-gradient(135deg,#e8e4de,#b59a84 55%,#6d5c52)" role="img" aria-label="Agent shaking hands with a client across a desk"></div>
<div class="abs" style="top:1103px;left:601px;width:539px;height:464px;background:var(--grey)"></div>
<div class="svc-text abs" style="top:1170px;left:664px;width:410px">
  <h3>Property Management</h3>
  <p>Lorem ipsum is simply dummy text of the printing and typesetting industry. Lorem Ipsum has been the industry's standard dummy text ever since the 1500s, when an unknown printer took a galley of type and scrambled it to make a type specimen book.</p>
  <p>It has survived not only five centuries, but also the leap into electronic typesetting, remaining essentially unchanged.</p>
  <a class="btn">Contact Us</a>
</div>
<div class="abs" style="top:1543px;left:570px;width:54px;height:54px;background:#fff;display:flex;align-items:center;justify-content:center;z-index:2"><span style="width:30px;height:30px;background:var(--gold)"></span></div>
<div class="abs" style="top:1567px;left:60px;width:541px;height:465px;background:var(--grey)"></div>
<div class="svc-text abs" style="top:1635px;left:124px;width:410px">
  <h3>Second-hand property sales</h3>
  <p>Lorem ipsum is simply dummy text of the printing and typesetting industry. Lorem Ipsum has been the industry's standard dummy text ever since the 1500s, when an unknown printer took a galley of type and scrambled it to make a type specimen book.</p>
  <p>It has survived not only five centuries, but also the leap into electronic typesetting, remaining essentially unchanged.</p>
  <a class="btn">Sell Now</a>
</div>
<div class="photo abs" style="top:1567px;left:601px;width:539px;height:465px;background:linear-gradient(135deg,#6b4a32,#c9c6c0 45%,#e9e7e3 70%,#8a6a4c)" role="img" aria-label="Bright living room with grey sofa and timber walls"></div>

<h2 class="h2 abs" style="top:2258px;left:0;width:1200px">See How Much You Can Save</h2>
<div class="save-card abs" style="top:2332px;left:325px"><small>YOU SAVE</small><b>$74,000</b><span>Buying With Verindale</span></div>
<div class="save-card abs" style="top:2332px;left:616px"><small>YOU SAVE</small><b>$1,41,000</b><span>Buying With Verindale</span></div>
<div class="abs" style="top:2494px;left:493px;width:120px;height:50px;border:1px solid #cfcfd6;text-align:center;background:#fff;padding-top:5px"><small style="font-size:10px;display:block">Your Home value</small><span style="font-size:15px">$74,000</span></div>
<svg class="abs" style="top:2535px;left:268px" width="664" height="60" viewBox="0 0 664 60" fill="none">
  <path d="M12 16l10-8 10 8v10H12z" stroke="#555" stroke-width="1.5"/>
  <path d="M628 16l10-8 10 8v10h-20z" stroke="#555" stroke-width="1.5"/>
  <line x1="80" y1="27" x2="606" y2="27" stroke="#e3e3e8" stroke-width="3"/>
  <line x1="80" y1="27" x2="285" y2="27" stroke="#efb940" stroke-width="3"/>
  <circle cx="285" cy="27" r="8" fill="#fff" stroke="#efb940" stroke-width="2.5"/>
</svg>
<div class="abs" style="top:2570px;left:268px;font-size:12px;font-weight:500">$50,000</div>
<div class="abs" style="top:2570px;left:892px;font-size:12px;font-weight:500">$2,00,000</div>
<a class="btn abs" style="top:2639px;left:492px;font-size:12px;padding:6px 14px">Sell House</a>
<a class="btn-ghost abs" style="top:2641px;left:603px;font-size:12px;padding:6px 14px">Buy House</a>
<div class="abs" style="top:2700px;left:0;width:1200px;text-align:center;font-size:13px">Have question? Call us <span style="color:var(--gold);font-size:15px">02 6200 4417</span></div>

<section class="listings abs"></section>
<h2 class="h2 abs" style="top:2852px;left:0;width:1200px">Listings Available For Latest Property</h2>
<div class="tabs abs"><div class="on">For Sale</div><div>For Lease</div><div>Open Times</div><div>Sold</div><div>Leased</div></div>

<div class="arrow fill abs" style="top:3180px;left:14px"><svg width="10" height="12" viewBox="0 0 10 12"><path d="M7 1L2 6l5 5" stroke="#fff" stroke-width="1.6" fill="none"/></svg></div>
<div class="arrow abs" style="top:3180px;left:1156px"><svg width="10" height="12" viewBox="0 0 10 12"><path d="M3 1l5 5-5 5" stroke="#1f2330" stroke-width="1.6" fill="none"/></svg></div>

<article class="card abs" style="left:60px">
  <span class="tag">On Sale</span>
  <div class="img" style="background:linear-gradient(160deg,#9fc4e6,#c9c9c9 50%,#4f7a3a)" role="img" aria-label="Apartment building with trees"></div>
  <div class="price">$369,000+</div>
  <div class="body"><h4>Gungahlin</h4>
    <div class="addr"><svg width="10" height="13" viewBox="0 0 10 13" fill="none" stroke="#efb940"><path d="M5 12S1 7 1 5a4 4 0 0 1 8 0c0 2-4 7-4 7z"/><circle cx="5" cy="5" r="1.5"/></svg>12/40 Ferris Street Belconnen...</div>
    <div class="feat"><span>▭ 1</span><span>◡ 1</span><span>▱ 1</span></div>
    <div class="insp">Next Inspection:</div><div class="date">Sat 21st May 9:40 Am-10:00 Am</div></div>
  <div class="agent"><span class="avatar"></span>Lena Hart<span class="tools">◷ ⤢ ✉</span></div>
</article>
<article class="card abs" style="left:429px">
  <span class="tag">On Sale</span>
  <div class="img" style="background:linear-gradient(170deg,#a9cbe8,#d0cfca 45%,#3a8fb8)" role="img" aria-label="Apartment tower beside a swimming pool"></div>
  <div class="price">$5,00,000+</div>
  <div class="body"><h4>Gungahlin</h4>
    <div class="addr"><svg width="10" height="13" viewBox="0 0 10 13" fill="none" stroke="#efb940"><path d="M5 12S1 7 1 5a4 4 0 0 1 8 0c0 2-4 7-4 7z"/><circle cx="5" cy="5" r="1.5"/></svg>Level 3/22 Marlow Crescent...</div>
    <div class="feat"><span>▭ 2</span><span>◡ 2</span><span>▱ 1</span></div>
    <div class="insp">Next Inspection:</div><div class="date">Sat 21st May 9:40 Am-10:00 Am</div></div>
  <div class="agent"><span class="avatar"></span>Lena Hart<span class="tools">◷ ⤢ ✉</span></div>
</article>
<article class="card abs" style="left:798px">
  <span class="tag">On Sale</span>
  <div class="img" style="background:linear-gradient(170deg,#7fa8d0,#8a7a6e 50%,#3e4a35)" role="img" aria-label="Suburban house with double garage"></div>
  <div class="price">$5,00,000+</div>
  <div class="body"><h4>Gungahlin</h4>
    <div class="addr"><svg width="10" height="13" viewBox="0 0 10 13" fill="none" stroke="#efb940"><path d="M5 12S1 7 1 5a4 4 0 0 1 8 0c0 2-4 7-4 7z"/><circle cx="5" cy="5" r="1.5"/></svg>Level 3/22 Marlow Crescent...</div>
    <div class="feat"><span>▭ 2</span><span>◡ 2</span><span>▱ 1</span></div>
    <div class="insp">Next Inspection:</div><div class="date">Sat 21st May 9:40 Am-10:00 Am</div></div>
  <div class="agent"><span class="avatar"></span>Lena Hart<span class="tools">◷ ⤢ ✉</span></div>
</article>
<a class="btn abs" style="top:3456px;left:550px;font-size:12px;padding:6px 14px">View More</a>

<section class="who-photo abs" role="img" aria-label="Modern concrete house surrounded by trees"></section>
<div class="who-box abs">
  <h2>Who Is Verindale Estates?</h2>
  <p>Verindale is a name that means "the home, the house", buying a property is one of the most expensive and important assets for people. Verindale Estates is a real estate company located in Gungahlin, Canberra.</p>
  <p>Being a portfolio sales agent and property manager, coupled with our high-profile international real estate experience, Verindale is considered a market leader on the cutting edge with deep industry knowledge, ranging from landlord-tenant relationships, residential purchases.</p>
  <p class="note">FOR CONFIDENTIALITY REASONS,20 TO 30% OF OUR PROPERTIES PLEASE CALL US FOR MORE INFORMATION</p>
  <a class="btn" style="margin-top:30px;font-size:12px;padding:6px 14px">More About</a>
</div>

<h2 class="h2 abs" style="top:4414px;left:0;width:1200px">What Our People Says</h2>
<div class="abs" style="top:4475px;left:0;width:1200px;text-align:center;font-size:60px;color:var(--gold);line-height:60px;font-weight:600">“</div>
<p class="abs" style="top:4528px;left:350px;width:500px;text-align:center;font-size:12.5px;line-height:23px;color:var(--text)">I would highly recommend Verindale property to you, they were helping me manage my investment property. they found a quality tenant in 2 days and maintain my property in a really good condition, they will update everything with me all the time and settle my worries. Maren, who is my PM, she is very patient and professional. I have had a bad property management experience, hence, I have had lots worries and questions, but Maren gained my trust and has done a really good job.</p>
<div class="abs" style="top:4690px;left:0;width:1200px;text-align:center;font-size:12.5px;font-weight:500">Tessa R.</div>
<div class="arrow fill abs" style="top:4580px;left:211px;width:36px;height:36px"><svg width="10" height="12" viewBox="0 0 10 12"><path d="M7 1L2 6l5 5" stroke="#fff" stroke-width="1.6" fill="none"/></svg></div>
<div class="arrow abs" style="top:4580px;left:937px;width:36px;height:36px"><svg width="10" height="12" viewBox="0 0 10 12"><path d="M3 1l5 5-5 5" stroke="#1f2330" stroke-width="1.6" fill="none"/></svg></div>

<section class="cta abs">
  <h2>Contact Us If You Want To Sell Your House Or You<br>Have Other Questions</h2>
  <a class="btn" style="font-size:12px;padding:6px 16px">Request Free Consultation</a>
</section>

<footer class="footer">
  <div class="abs" style="top:5050px;left:60px;width:220px">
    <div class="brand" style="font-size:26px"><span class="mark" style="width:38px;height:38px"></span>Verindale</div>
    <p style="margin-top:32px">Lorem ipsum dolor sit amet, consectetur adipiscing elit, sed do eiusmod tempor...</p>
  </div>
  <div class="abs" style="top:5045px;left:332px">
    <h5>Site Map</h5>
    <ul><li>Home</li><li>About Us</li><li>Leasing</li><li>Buy</li><li>Sell</li><li>Our Team</li><li>Blog</li><li>Contact Us</li></ul>
  </div>
  <div class="abs" style="top:5045px;left:613px;width:240px">
    <h5>Contact Us</h5>
    <div style="display:flex;gap:12px;font-size:12px;line-height:20px"><svg width="18" height="20" viewBox="0 0 18 20" fill="none" stroke="#1f2330"><path d="M9 19S2 11 2 7a7 7 0 0 1 14 0c0 4-7 12-7 12z"/><circle cx="9" cy="7" r="2.5"/></svg><span>18/5 Marlow Crescent,<br>Gungahlin, ACT, 2912</span></div>
    <div style="display:flex;gap:12px;font-size:12px;margin-top:14px;font-weight:600;line-height:24px"><svg width="18" height="18" viewBox="0 0 18 18" fill="none" stroke="#1f2330"><path d="M4 1l3 4-2 2a10 10 0 0 0 6 6l2-2 4 3-2 3C8 17 1 10 1 3z"/></svg><span>02 6200 4417<br>02 6200 4418</span></div>
    <div style="display:flex;gap:12px;font-size:12px;margin-top:14px"><svg width="18" height="14" viewBox="0 0 18 14" fill="none" stroke="#1f2330"><rect x="1" y="1" width="16" height="12"/><path d="M1 1l8 7 8-7"/></svg>info@verindaleestates.com.au</div>
  </div>
  <div class="abs" style="top:5045px;left:890px">
    <h5>Follow On Us</h5>
    <div class="social" aria-label="Social media links"><div class="first"></div><div></div><div></div><div></div></div>
  </div>
  <div class="bottom-bar abs">
    <span>2022© Verindale Estates. All right reserved.</span>
    <nav><span>Privacy</span><span>Complaint Handling &amp; Dispute Resolution</span><span>Due Diligence Checklist</span></nav>
  </div>
</footer>

</body>
</html>
```